Brightquarry.com home page

On the existing home page I want to eliminate people in circles and promote these three earning opportunities:
1." Make a referral to existing advertiser"
Earn up to $5000 when you make a successful referral to one of our advertisers.
2."Sign up a new business to offer referral commisions to ambassaadors". Earn up to $5000 or more when you earn 5% of money paid out by business in referral fees.
3."Sign up new ambassadors"
Earn up to $5000 or more when you earn 5% of the money the ambassadors you sign up earn.

In each offer I want a learn more button .

Business

Serif

```html
<!DOCTYPE html>
<html lang="en">
<head>
<meta charset="utf-8">
<title>BrightQuarry – Referral Marketplace</title>
<link rel="stylesheet" href="https://fonts.googleapis.com/css2?family=Roboto+Condensed:ital,wght@0,300;0,400;0,700;1,700&family=Open+Sans:wght@400;600;700&display=swap">
<style>
  :root {
    --green: #2bb05f;
    --green-dark: #1f9a4f;
    --grey-bg: #f0f0f0;
    --white: #ffffff;
    --ink: #111111;
    --nav-text: #555555;
    --muted: #7d8a8a;
    --black: #000000;
  }
  * { margin: 0; padding: 0; box-sizing: border-box; }
  html, body { width: 1200px; height: 631px; overflow: hidden; }
  body {
    background: var(--grey-bg);
    font-family: "Roboto Condensed", "Arial Narrow", sans-serif;
    position: relative;
  }

  /* Header */
  .site-header {
    position: absolute; left: 0; top: 0;
    width: 1200px; height: 77px;
    background: var(--white);
  }
  .brand { position: absolute; left: 17px; top: 12px; }
  .brand-name {
    font-family: "Open Sans", sans-serif;
    font-weight: 600;
    font-size: 37px;
    line-height: 40px;
    letter-spacing: -1px;
    color: var(--green);
  }
  .brand-tagline {
    font-family: "Open Sans", sans-serif;
    font-size: 11px;
    color: var(--muted);
    letter-spacing: 0.3px;
    margin-left: 2px;
    margin-top: -1px;
  }
  .main-nav { position: absolute; top: 0; left: 733px; height: 77px; }
  .main-nav a {
    position: absolute; top: 0; height: 77px;
    line-height: 77px;
    font-family: "Open Sans", sans-serif;
    font-size: 14.5px;
    color: var(--nav-text);
    text-decoration: none;
    white-space: nowrap;
  }
  .main-nav a.is-active {
    left: 0; width: 72px; text-align: center;
    background: var(--green); color: var(--white);
  }
  .nav-how { left: 88px; }
  .nav-search { left: 209px; }
  .nav-members { left: 286px; }
  .nav-login { left: 378px; }

  /* Offers */
  .offer {
    position: absolute; left: 66px; width: 928px;
    background: var(--white);
    border-radius: 16px;
    padding: 16px 18px 0 18px;
  }
  .offer::before {
    content: "";
    position: absolute; left: 32px; bottom: -8px;
    width: 760px; height: 9px;
    background: var(--black);
    filter: blur(2.5px);
    border-radius: 0 0 40% 60%;
    transform: skewX(-20deg);
    z-index: -1;
  }
  .offer-title {
    font-weight: 700;
    font-size: 33px;
    line-height: 33px;
    color: var(--green);
    text-transform: uppercase;
    letter-spacing: 0.2px;
  }
  .offer-title .indent { padding-left: 16px; }
  .offer-text {
    font-weight: 700;
    font-size: 21px;
    line-height: 26px;
    color: var(--ink);
    margin-top: 6px;
  }
  .offer-referral { top: 108px; height: 101px; padding-top: 21px; }
  .offer-business { top: 245px; height: 124px; padding-left: 14px; padding-top: 10px; }
  .offer-business .offer-title { padding-left: 0; }
  .offer-ambassadors { top: 408px; height: 101px; padding-left: 14px; padding-top: 14px; }

  .learn-more {
    position: absolute; left: 976px; width: 153px; height: 47px;
    border-radius: 12px;
    background: linear-gradient(90deg, var(--green-dark) 0 8px, var(--green) 8px calc(100% - 8px), var(--green-dark) calc(100% - 8px));
    color: var(--white);
    font-weight: 700; font-style: italic;
    font-size: 21px;
    line-height: 47px;
    text-align: center;
    text-decoration: none;
  }
  .learn-referral { top: 135px; }
  .learn-business { top: 279px; }
  .learn-ambassadors { top: 434px; }

  /* Footer band */
  .signup-band {
    position: absolute; left: 0; top: 553px;
    width: 1200px; height: 78px;
    background: var(--green);
  }
  .signup-pitch {
    position: absolute; left: 19px; top: 0;
    line-height: 64px;
    font-weight: 300;
    font-size: 24px;
    color: var(--white);
    white-space: nowrap;
  }
  .signup-button {
    position: absolute; left: 959px; top: 9px;
    width: 215px; height: 53px;
    background: var(--black);
    border-radius: 5px;
    color: var(--white);
    font-weight: 700; font-style: italic;
    font-size: 28px;
    line-height: 53px;
    text-align: center;
    text-decoration: none;
  }
</style>
</head>
<body>
  <header class="site-header">
    <div class="brand">
      <div class="brand-name">BrightQuarry</div>
      <div class="brand-tagline">Referral Marketplace</div>
    </div>
    <nav class="main-nav">
      <a class="is-active" href="#">Home</a>
      <a class="nav-how" href="#">How It Works</a>
      <a class="nav-search" href="#">Search</a>
      <a class="nav-members" href="#">Members</a>
      <a class="nav-login" href="#">Log In</a>
    </nav>
  </header>

  <main>
    <section class="offer offer-referral">
      <h2 class="offer-title">"Make a referral to existing advertiser"</h2>
      <p class="offer-text">Earn up to $5000 when you make a successful referral to one of our advertisers.</p>
    </section>
    <a class="learn-more learn-referral" href="#">Learn more</a>

    <section class="offer offer-business">
      <h2 class="offer-title">"Sign up a new business to offer referral<br><span class="indent">commisions to ambassaadors"</span></h2>
      <p class="offer-text">Earn up to $5000 or more when you earn 5% of money paid out by business in referral fees.</p>
    </section>
    <a class="learn-more learn-business" href="#">Learn more</a>

    <section class="offer offer-ambassadors">
      <h2 class="offer-title">"Sign up new ambassadors"</h2>
      <p class="offer-text">Earn up to $5000 or more when you earn 5% of the money the ambassadors you sign up earn.</p>
    </section>
    <a class="learn-more learn-ambassadors" href="#">Learn more</a>
  </main>

  <footer class="signup-band">
    <p class="signup-pitch">BrightQuarry, Fastest Growing Referral Marketplace. Earn income just by referring people you know.</p>
    <a class="signup-button" href="#">Free to sign up</a>
  </footer>
</body>
</html>
```